Kessler MD Summit Primary Care Business Card

Need a business card for a medical clinic targeting VIP patients. Should portray an upscale feeling. Simple, clean design. Logo and colors need to be incorporated into card. Clinic colors are gray/ silver, blues, white same as logo.
Clinic is a cash only VIP service clinic targeting higher income patients.
Tagline: "Where everyone is a VIP - Very Important Patient"

Target Market(s)

VIP, upscale

Industry/Entity Type

Medical

Contact Information for Business Card

Would like to use for cards with raised print or metallic highlight.

Requirements
Must have
• Incorporate logo, Use colors in logo
Nice to have
• Metallic detail
Should not have
• too much details or colors, other stock photos or designs

```html
<!DOCTYPE html>
<html lang="en">
<head>
<meta charset="utf-8">
<title>Kessler MD Summit Primary Care — Business Card</title>
<link href="https://fonts.googleapis.com/css2?family=Cinzel:wght@400;700&family=Lato:wght@400;700&display=swap" rel="stylesheet">
<style>
  :root {
    --slate: #435670;
    --slate-dark: #3a4b63;
    --silver: #9aa0a6;
    --silver-light: #c9cdd2;
    --ink: #3c4a5e;
    --paper: #ffffff;
    --backdrop: #eceae6;
    --rule: #8a8f96;
  }
  * { box-sizing: border-box; margin: 0; padding: 0; }
  html, body {
    width: 1200px; height: 900px; overflow: hidden;
    background: var(--backdrop);
  }
  .stage { position: relative; width: 1200px; height: 900px; }

  .card {
    position: absolute;
    width: 560px; height: 320px;
    background: var(--paper);
    overflow: hidden;
    box-shadow: 0 6px 18px rgba(0,0,0,.14);
  }

  /* Appointment side */
  .card--appointment { left: 60px; top: 130px; }
  .appointment__band {
    height: 140px;
    background: var(--slate);
    display: flex; flex-direction: column; align-items: center; justify-content: center;
    gap: 4px;
  }
  .clinic-title {
    display: flex; align-items: center; gap: 14px;
    font-family: "Cinzel", serif; font-weight: 400;
    color: var(--silver-light);
    font-size: 25px; letter-spacing: 1px; line-height: 1.05;
  }
  .clinic-title__rule { width: 46px; height: 1px; background: var(--silver-light); }
  .clinic-subtitle {
    font-family: "Cinzel", serif; font-weight: 400;
    color: var(--silver-light); font-size: 25px; letter-spacing: 1px; line-height: 1.05;
  }
  .tagline {
    margin-top: 8px;
    font-family: "Lato", sans-serif; font-weight: 700;
    color: var(--paper); font-size: 13.5px; letter-spacing: .4px;
  }
  .appointment__fields { padding: 40px 60px 0 70px; }
  .field { display: flex; align-items: flex-end; gap: 14px; height: 44px; }
  .field__label {
    font-family: "Cinzel", serif; font-size: 17px; color: var(--ink);
    width: 62px;
  }
  .field__line { flex: 1; height: 1px; background: var(--rule); margin-bottom: 6px; }

  /* Contact side */
  .card--contact { left: 580px; top: 450px; }
  .contact__wave { position: absolute; inset: 0; }
  .person { position: absolute; left: 36px; top: 58px; }
  .person__name {
    font-family: "Cinzel", serif; font-weight: 700; font-size: 19px;
    color: var(--slate); letter-spacing: .5px;
  }
  .person__name span { color: var(--silver); }
  .person__role {
    font-family: "Lato", sans-serif; font-size: 13px; color: var(--ink);
  }
  .contact-list {
    position: absolute; left: 56px; top: 150px;
    list-style: none;
    font-family: "Lato", sans-serif; font-size: 14px; color: var(--ink);
  }
  .contact-list li { display: flex; align-items: center; gap: 8px; height: 19px; }
  .contact-list svg { width: 12px; height: 12px; fill: var(--slate); flex: none; }
  .contact-address {
    position: absolute; left: 56px; top: 222px;
    font-family: "Lato", sans-serif; font-size: 14px; line-height: 1.4; color: var(--ink);
  }
  .brand {
    position: absolute; right: 30px; top: 46px; width: 230px;
    display: flex; flex-direction: column; align-items: center; gap: 8px;
  }
  .brand__mark { width: 28px; height: 28px; border-radius: 50%; background: var(--slate); }
  .brand__name {
    font-family: "Cinzel", serif; font-weight: 400; font-size: 16px;
    color: var(--slate); text-align: center; line-height: 1.2; letter-spacing: .5px;
  }
  .website {
    position: absolute; right: 28px; top: 222px;
    font-family: "Lato", sans-serif; font-size: 12px; color: var(--paper);
  }
</style>
</head>
<body>
<main class="stage">

  <section class="card card--appointment" aria-label="Appointment side">
    <header class="appointment__band">
      <div class="clinic-title"><span class="clinic-title__rule"></span>KESSLER MD<span class="clinic-title__rule"></span></div>
      <div class="clinic-subtitle">SUMMIT PRIMARY CARE</div>
      <p class="tagline">WHERE EVERYONE IS A VIP - VERY IMPORTANT PATIENT</p>
    </header>
    <div class="appointment__fields">
      <div class="field"><span class="field__label">DATE</span><span class="field__line"></span></div>
      <div class="field"><span class="field__label">TIME</span><span class="field__line"></span></div>
    </div>
  </section>

  <section class="card card--contact" aria-label="Contact side">
    <svg class="contact__wave" viewBox="0 0 560 320" preserveAspectRatio="none" aria-hidden="true">
      <path d="M0,258 C140,292 280,268 375,205 C410,182 440,165 468,152 C430,178 400,200 362,225 C265,285 130,292 0,270 Z" fill="var(--silver)"/>
      <path d="M0,288 C150,312 290,295 370,235 C440,185 500,150 560,130 L560,320 L0,320 Z" fill="var(--slate)"/>
    </svg>

    <div class="person">
      <h1 class="person__name">DANIEL <span>WHITFORD</span></h1>
      <p class="person__role">Managing Director</p>
    </div>

    <ul class="contact-list">
      <li><svg viewBox="0 0 12 12"><path d="M1 3c0-1 1-2 2-2h6c1 0 2 1 2 2v1H8V3H4v1H1zM2 5h8l1 6H1z"/></svg>(044) 123456789</li>
      <li><svg viewBox="0 0 12 12"><path d="M3 0h6v12H3zM4 1v8h4V1z"/></svg>(044)123456789</li>
      <li><svg viewBox="0 0 12 12"><path d="M0 2h12v8H0zM1 3l5 4 5-4z" fill-rule="evenodd"/></svg>info@youremail.com</li>
    </ul>
    <p class="contact-address">1234, Address GoesHere,<br>Country, 12345</p>

    <div class="brand">
      <span class="brand__mark"></span>
      <p class="brand__name">KESSLER MD<br>SUMMIT PRIMARY CARE</p>
    </div>

    <p class="website">www.yourwebsite.com</p>
  </section>

</main>
</body>
</html>
```